PIPE RELINING COMPANY NEEDS A NEW INFORMATIVE FLYER CREATED

We are a company that sells a service to residential homeowners (using a particular state of the art international product) and we need to refresh our A4 tri- fold flyer (z fold 6 pages). The layout needs to include pictures, heading and text boxes, but be simple and clean cut at the same time.

The front of the flyer must have the attached picture of the pipe under the house, logo and website.

This flyer is going to be given to clients and to leave with them when we quote for work.

Our colour scheme is black, white, red. A highlight colour if needed (in small amounts) could be 100% cyan and also a bright orange.

I have attached the copy of the text and this can be spread out throughout the brochure.

We are a professional and industry leading company so it needs to be professional, clean cut but with a modern edge.

Target Market(s)

HOMEOWNERS

Industry/Entity Type

It Company

Font styles to use
Sans Serif

Colors
ec1f27
ffffff
000000
f37122

Requirements
Must have
• PROFESSINAL, MODERN
• USE OF BLACK, RED AND WHITE - REFER LOGO
Should not have
• BE CLUTTERED

```html
<!DOCTYPE html>
<html lang="en">
<head>
<meta charset="utf-8">
<title>A New Pipe within the old – Pipe Relining Flyer</title>
<link rel="stylesheet" href="https://fonts.googleapis.com/css2?family=PT+Sans:wght@400;700&family=Roboto:ital,wght@0,700;0,900;1,900&display=swap">
<style>
  :root{
    --red:#ec1f27;
    --black:#000000;
    --white:#ffffff;
    --orange:#f37122;
    --yellow:#ffd21f;
    --ink:#1a1a1a;
  }
  *{margin:0;padding:0;box-sizing:border-box}
  html,body{width:1200px;height:873px;overflow:hidden;background:var(--black)}
  .flyer{position:relative;width:1200px;height:873px;background:var(--black);font-family:"PT Sans",Arial,sans-serif;color:var(--ink)}
  .sheet{position:absolute;left:40px;top:40px;width:1121px;height:792px;background:var(--red);border:1px solid #f4d6d6}

  .title-band{position:absolute;left:0;top:0;width:100%;height:58px;display:flex;align-items:center;justify-content:center}
  .title-band h1,.footer-band p{font-family:"Roboto",Arial,sans-serif;font-weight:900;font-style:italic;color:var(--white);font-size:30px;letter-spacing:.3px}
  .footer-band{position:absolute;left:0;bottom:0;width:100%;height:58px;display:flex;align-items:center;justify-content:center}
  .footer-band p{font-size:26px;letter-spacing:.6px}

  .column{position:absolute;top:58px;height:676px}
  .column--left{left:0;width:374px;background:var(--white);padding:10px 15px 0 16px}
  .column--middle{left:374px;width:374px;padding:10px 15px 0 16px;color:var(--white)}
  .column--right{left:748px;width:373px;background:var(--white);padding:8px 13px 0 16px}

  .wedge{position:absolute}
  .wedge--left{left:0;top:670px}
  .wedge--right{right:0;top:0}

  .bullets{list-style:none}
  .bullets li{position:relative;padding-left:26px;font-size:14.5px;line-height:18.6px;margin-bottom:0}
  .bullets li::before{content:"";position:absolute;left:1px;top:6px;width:7px;height:7px;background:var(--red)}
  .bullets--intro li{text-align:justify}

  .heading{font-family:"Roboto",Arial,sans-serif;font-weight:900;color:var(--orange);font-size:19.5px;line-height:19px;text-transform:uppercase;letter-spacing:.2px}
  .heading--light{color:var(--yellow)}
  .body{font-size:14.5px;line-height:18.6px;text-align:justify}
  .body b{font-weight:700}

  .column--left .heading{margin-top:20px;margin-bottom:1px}
  .column--middle .heading{margin-bottom:3px}
  .column--middle .body{color:#ffe9e9}

  .process{list-style:none;font-family:"Roboto",Arial,sans-serif;font-weight:700;font-size:12.4px;line-height:18.7px;color:var(--white);text-align:justify;letter-spacing:.15px}
  .process li{position:relative;padding-left:22px}
  .process li::before{content:"";position:absolute;left:2px;top:7px;width:6px;height:6px;background:var(--yellow)}

  .middle-benefits .body{color:var(--white)}

  .photo{position:absolute;top:617px;width:92px;height:96px;border-radius:4px;border:2px solid #3a3a3a}
  .photo--before{left:160px;background:linear-gradient(160deg,#c7a89b,#9b7b6f)}
  .photo--after{left:267px;background:linear-gradient(160deg,#5fae3f,#3f8a2c)}
  .photo-label{position:absolute;top:716px;width:92px;text-align:center;font-weight:700;font-size:14.5px;line-height:17px;color:var(--ink);z-index:2}
  .photo-label--before{left:160px}
  .photo-label--after{left:267px}

  .pipe-photo{position:absolute;right:4px;top:6px;width:112px;height:118px;border-radius:12px;background:linear-gradient(150deg,#6bbb4e,#c98a6e)}

  .benefit-list .body{margin-bottom:3px}
  .column--right .heading{margin-top:22px;margin-bottom:3px}
</style>
</head>
<body>
<div class="flyer">
  <div class="sheet">
    <header class="title-band"><h1>A New Pipe within the old</h1></header>

    <section class="column column--left">
      <ul class="bullets bullets--intro">
        <li>Sewers back up in properties due to ageing lines, misaligned joints, root infestation, calcification and ground movement, costing property owners thousands of dollars in damage to their homes and landscaping.</li>
        <li>Pipe relining eliminates the need for costly excavations to expose and replace this damaged pipework.</li>
        <li>Pipe Relining is the process of installing a new pipe within the old.</li>
        <li>Why replace all of your drainage pipes when you can permanently repair the broken sections without destroying your environment.</li>
      </ul>
      <h2 class="heading">What does<br>pipe relining mean?</h2>
      <p class="body">Pipe relining is the method of repairing existing pipe work from within the pipe itself. This is done by using the latest technology to insert a strong internal liner inside the existing pipe.</p>
      <p class="body">&nbsp;During this process the resin impregnated side of the liner is pressed against the wall of the original host pipe at a specified pressure. This pressure ensure 100% resin contact and extrudes resin into all pipe joints, cracks and breaks ensuring no future tree root ingress or pipe movement is possible.</p>
      <p class="body">Pipe relining can be undertaken in either short sectional repair, or long lengths utilising the inversion relining method.</p>
    </section>
    <svg class="wedge wedge--left" width="190" height="64" viewBox="0 0 190 64" aria-hidden="true"><polygon points="0,0 80,0 180,64 0,64" fill="#ec1f27"/></svg>
    <div class="photo photo--before" role="img" aria-label="Camera view inside a cracked, root-infested pipe before relining"></div>
    <div class="photo photo--after" role="img" aria-label="Camera view inside a smooth green relined pipe after repair"></div>
    <span class="photo-label photo-label--before">Before</span>
    <span class="photo-label photo-label--after">After</span>

    <section class="column column--middle">
      <h2 class="heading heading--light">Which problems<br>can pipe relining repair?</h2>
      <p class="body">Pipe relining can repair broken, cracked or root infested pipes, pipes with missing sections and pipes that continually block.</p>
      <p class="body">No matter if the pipes are vertical, horizontal or concealed, they all can be repaired. Sections of broken pipes can be relined, without having to replace the entire pipeline.</p>
      <h2 class="heading heading--light" style="margin-top:17px">Patch repair process</h2>
      <ul class="process">
        <li>Clean the line with a high pressure water jetter, and carry out a camera inspection to determine the exact location and cause of the problems.</li>
        <li>Prepare the liner. Cut the liner to the correct length, mix the appropriate amount of rein and impregnate the rein into the liner.</li>
        <li>Invert the liner into the pipe, inflate and then cure.</li>
        <li>A seamless, flexible liner is cut to length and filled with environmentally safe epoxy rein. The liner is them inverted into the existing, host pipe and inflated using compressed air. Once the liner is fully cured with hot water, it is ready for use.</li>
        <li>The result is a completely new pipe inside the old. This pipe within a pie is 100% water tight, stronger than PVC pipe, and has an increased flow rate compared to most existing pipes. Relined pipes have a life expectancy of 50 years and our installation work has a 25 year guarantee.</li>
      </ul>
      <div class="middle-benefits">
        <h2 class="heading heading--light" style="margin-top:18px">Benefits of pipe relining</h2>
        <p class="body"><b>Quick Installation</b> – Most relining jobs can be completed in the same day-without tht mess and disruption of excavation.</p>
      </div>
    </section>

    <section class="column column--right">
      <svg class="wedge wedge--right" width="180" height="68" viewBox="0 0 180 68" aria-hidden="true"><polygon points="0,0 180,0 180,68 78,68" fill="#ec1f27"/></svg>
      <div class="benefit-list" style="position:relative">
        <p class="body" style="text-align:left"><b>Long Life Product</b> –<br>Pipe Relining is a long term solution<br>with a 50 year life expectancy.</p>
        <p class="body"><b>Minimal Disruption</b> – ave your landscapes, trees and driveways.</p>
        <p class="body"><b>Economical</b> – Save on the cost, time and hassle of restoring your property and landscaping.</p>
        <p class="body"><b>Installation Guarantee</b> – Boreline offer a 25 year warranty, twice that of standard excavations. This also includes an annual warranty camera inspection.</p>
        <p class="body">Provides a solution to the whole problem, not just temporary relief from the symptoms.</p>
      </div>
      <h2 class="heading">What does<br>pipe relining mean?</h2>
      <ul class="bullets">
        <li>Permanent jointless liner</li>
        <li>50 years life expectancy</li>
        <li>Up front price</li>
        <li>Environmentally sound</li>
        <li>Eliminates structural disturbances</li>
        <li>Impervious to future root penetration</li>
        <li>Provides increased flow characteristics</li>
        <li>Suitable for industrial, residential and commercial applications</li>
      </ul>
      <h2 class="heading" style="margin-top:18px">Things you should know</h2>
      <ul class="bullets">
        <li>Knowledge &amp; Experience</li>
        <li>We train other plumbers and have been doing it for over 10 years.</li>
        <li>We’re An Owned &amp; Operated Business</li>
        <li>We take great pride in our work. Our business is based on relationships not transactions.</li>
      </ul>
    </section>
    <div class="pipe-photo" role="img" aria-label="Cut-away pipe fitting showing a green liner inside an old clay pipe"></div>

    <footer class="footer-band"><p>A fast, clean, permanent solution&nbsp; for fixing blocked drains</p></footer>
  </div>
</div>
</body>
</html>
```